a simple functional website for an up and coming service industry business

hi ,i also require in store promotional items like business cards, flyers, plain square page t-shirts for workers and want all these to have the same look and feel.i need my website to catch the eye .the idea i have in my head is something that will sell the service ,the website is a tool to get people to inquire , book or pay for an assembly service.we assemble flatpack furniture , outdoor furniture,playgrounds etc ,basically anything that comes with instructions,our biggest customer at the moment is Norvalt who we assemble nationally.i am looking for a website to be bright modern and simple to use the current website is www.brindleyfitouts.com which is dull with to many pages . i have already had a new logo designed by sketch harbour and it is lime green and sky blue in colour, a webiste i like is jobtrek q4 although it has lots of flash and my budget probably wouldn't allow that at the moment.

Target Market(s)

customer will be visiting the website to find out about the service we provide , then hopefully making contact,either booking a job or asking for a quote, i like the idea of the phone, email icons on the home screen

Industry/Entity Type

Industry

Requirements
Must have
• a contact icon: when you click on it the page with the name ,email address ,phone number, address pops up

a phone icon : when you click on it the 1300 number pops up
Nice to have
• my current website is with plume and it is www.brindleyfitouts.com

a website i really like the design of is jobtrek q4 and Norvalt

would like some pictures of modern furniture ,bbq's ,gym equipment ,playground equiptment
Should not have
• the career page or price page my current website .i don't want it on there anymore

```html
<!DOCTYPE html>
<html lang="en">
<head>
<meta charset="utf-8">
<title>Brindley Assembly</title>
<link href="https://fonts.googleapis.com/css2?family=Play:wght@400;700&family=Alfa+Slab+One&family=Ubuntu:wght@500;700&family=Open+Sans:wght@400;700&display=swap" rel="stylesheet">
<style>
:root{
  --lime:#8dc63f;
  --sky:#2a8fd6;
  --ink:#3d3d3d;
  --muted:#6b6b6b;
  --rule:#c9c9c9;
  --paper:#ffffff;
  --btn:#5d6166;
}
*{box-sizing:border-box;margin:0;padding:0}
html,body{width:1200px;height:750px;overflow:hidden;background:#fff}
.site{position:relative;width:1200px;height:750px;overflow:hidden;font-family:"Play",sans-serif;color:var(--ink)}

.sidebar{position:absolute;left:0;top:0;width:234px;height:750px;background:var(--paper);border-right:3px solid #d4d4d4;z-index:2}
.brand{position:absolute;left:0;top:62px;width:234px;text-align:center}
.brand-mark{display:inline-block;width:40px;height:40px;background:var(--lime);border-radius:4px}
.brand-name{display:block;margin-top:8px;font-family:"Play",sans-serif;font-size:19px;font-weight:700;color:var(--sky);letter-spacing:.5px}

.main-nav{position:absolute;left:28px;top:202px;width:170px;list-style:none}
.main-nav li{height:33px;border-bottom:1px solid var(--rule);font-size:17px;line-height:30px;padding-left:11px;color:var(--muted);letter-spacing:.4px}
.main-nav li:last-child{border-bottom:none}

.quick-contact{position:absolute;top:354px;left:36px;display:flex;gap:18px}
.quick-btn{width:67px;height:67px;border:1px solid #d0d0d0;border-radius:6px;background:#fff;box-shadow:0 2px 4px rgba(0,0,0,.25);display:flex;align-items:center;justify-content:center}

.call-out{position:absolute;top:462px;left:0;width:234px;text-align:center}
.call-out-q{font-family:"Play",sans-serif;font-weight:700;font-size:20px;line-height:19px;color:var(--muted)}
.call-out-name{font-family:"Alfa Slab One",serif;font-size:27px;color:var(--sky);margin-top:6px;line-height:30px}
.call-out-number{font-family:"Ubuntu",sans-serif;font-weight:700;font-size:31px;color:#2e2e2e;line-height:36px}

.share{position:absolute;top:594px;left:16px;width:210px}
.share-text{font-family:"Play",sans-serif;font-size:15px;color:#8a9098;transform:rotate(-3deg);display:inline-block;margin-top:10px}
.share-arrow{position:absolute;right:0;top:0}
.social{position:absolute;top:643px;left:53px;display:flex;gap:3px}
.social span{width:29px;height:29px;border-radius:3px;background:var(--sky);box-shadow:0 1px 2px rgba(0,0,0,.3)}

.legal{position:absolute;top:690px;left:13px;width:203px;font-family:"Open Sans",sans-serif;font-size:9.5px;line-height:13px;color:#555}
.legal strong{display:block;text-align:right;color:#333}

.hero{position:absolute;left:237px;top:0;width:963px;height:750px;
  background:
    radial-gradient(ellipse at 25% 30%,#bfe4f4 0%,rgba(191,228,244,0) 45%),
    linear-gradient(180deg,#9fd3ee 0%,#6fb4e0 42%,#c9d4db 62%,#b3bcc2 100%)}
.hero-room{position:absolute;right:0;top:0;width:390px;height:480px;background:linear-gradient(180deg,#d9c9a6 0%,#3f6ec6 55%,#8cc63f 78%,#9aa7b1 100%);opacity:.7}

.slide-caption{position:absolute;left:747px;top:489px;z-index:1}
.caption-main{display:block;width:326px;height:46px;background:var(--sky);color:#fff;font-family:"Alfa Slab One",serif;font-size:29px;line-height:46px;padding-left:12px}
.caption-sub{display:inline-block;height:45px;background:var(--lime);color:#fff;font-family:"Play",sans-serif;font-size:26px;line-height:45px;padding:0 12px}

.slider-nav{position:absolute;left:1095px;top:685px;display:flex;gap:2px;z-index:1}
.slider-nav span{width:28px;height:28px;background:var(--btn);display:flex;align-items:center;justify-content:center}

.contact-popup{position:absolute;left:449px;top:241px;width:521px;height:265px;background:#fff;border-radius:14px;box-shadow:0 0 10px rgba(0,0,0,.35);z-index:3}
.popup-close{position:absolute;right:11px;top:11px}
.popup-brand{position:absolute;left:28px;top:28px;display:flex;align-items:center;gap:10px}
.popup-brand-mark{width:40px;height:40px;background:var(--lime);border-radius:4px}
.popup-brand-name{font-size:22px;font-weight:700;color:var(--sky);letter-spacing:.5px}
.popup-col{position:absolute;top:115px;font-size:13.5px;line-height:15px;color:#3a3a3a}
.popup-col h2{font-family:"Play",sans-serif;font-weight:700;font-size:20px;color:var(--sky);letter-spacing:.5px;margin-bottom:6px}
.popup-col .gap{margin-top:5px}
.col-general{left:23px}
.col-rep{left:277px}
.popup-divider{position:absolute;left:265px;top:101px;width:1px;height:139px;background:#bdbdbd}
</style>
</head>
<body>
<div class="site">

  <aside class="sidebar">
    <div class="brand">
      <span class="brand-mark"></span>
      <span class="brand-name">BRINDLEY ASSEMBLY</span>
    </div>

    <ul class="main-nav">
      <li>Home</li>
      <li>About Us</li>
      <li>Services</li>
      <li>Contact Us</li>
    </ul>

    <div class="quick-contact">
      <div class="quick-btn" aria-label="Email us">
        <svg width="44" height="34" viewBox="0 0 44 34">
          <rect x="2" y="3" width="40" height="28" rx="3" fill="#4fb3e3" stroke="#1f7fb8" stroke-width="2"/>
          <path d="M3 5 L22 19 L41 5" fill="none" stroke="#1f7fb8" stroke-width="2"/>
        </svg>
      </div>
      <div class="quick-btn" aria-label="Call us">
        <svg width="42" height="36" viewBox="0 0 42 36">
          <path d="M4 10 Q21 0 38 10 L36 15 L29 13 L28 9 Q21 7 14 9 L13 13 L6 15 Z" fill="#2a8fd6"/>
          <path d="M9 17 L33 17 L37 33 L5 33 Z" fill="#3aa3e4" stroke="#1f7fb8" stroke-width="1.5"/>
          <circle cx="21" cy="25" r="5" fill="#fff"/>
        </svg>
      </div>
    </div>

    <div class="call-out">
      <p class="call-out-q">Got a Question?<br>Call us!</p>
      <p class="call-out-name">brindley</p>
      <p class="call-out-number">1300-555-214</p>
    </div>

    <div class="share">
      <span class="share-text">Liked this post? share it!</span>
      <svg class="share-arrow" width="30" height="34" viewBox="0 0 30 34">
        <path d="M4 6 Q22 -2 26 16 L24 30" fill="none" stroke="#8a9098" stroke-width="1.5"/>
        <path d="M19 25 L24 31 L28 24" fill="none" stroke="#8a9098" stroke-width="1.5"/>
      </svg>
    </div>
    <div class="social" aria-label="Share links">
      <span></span><span></span><span></span><span></span>
    </div>

    <p class="legal">© 2013 BRINDLEY FITOUTS PTY LTD<strong>QBSA LICENCE NUMBER: 4410273</strong></p>
  </aside>

  <section class="hero" role="img" aria-label="Photo of a bright modern children's bedroom with blue walls, lime green furniture, shelving, a desk and a toy giraffe">
    <div class="hero-room"></div>
  </section>

  <div class="slide-caption">
    <span class="caption-main">Domestic Fit Outs</span>
    <span class="caption-sub">Nurseries</span>
  </div>

  <div class="slider-nav">
    <span><svg width="10" height="12" viewBox="0 0 10 12"><path d="M8 1 L2 6 L8 11" fill="none" stroke="#fff" stroke-width="2"/></svg></span>
    <span><svg width="10" height="12" viewBox="0 0 10 12"><path d="M2 1 L8 6 L2 11" fill="none" stroke="#fff" stroke-width="2"/></svg></span>
  </div>

  <div class="contact-popup" role="dialog" aria-label="Contact details">
    <svg class="popup-close" width="22" height="22" viewBox="0 0 22 22">
      <circle cx="11" cy="11" r="9.5" fill="#fff" stroke="#b5b5b5" stroke-width="1.5"/>
      <path d="M7.5 7.5 L14.5 14.5 M14.5 7.5 L7.5 14.5" stroke="#9a9a9a" stroke-width="1.5"/>
    </svg>
    <div class="popup-brand">
      <span class="popup-brand-mark"></span>
      <span class="popup-brand-name">BRINDLEY ASSEMBLY</span>
    </div>

    <div class="popup-col col-general">
      <h2>GENERAL</h2>
      <p>P 1300 555 214 [M to F]</p>
      <p>E admin@brindleyfitouts.com</p>
      <p>PO Box 2071</p>
      <p>Kelvin Ridge</p>
      <p class="gap">Brisbane QLD 4199</p>
    </div>
    <div class="popup-divider"></div>
    <div class="popup-col col-rep">
      <h2>LOCAL REP</h2>
      <p>Dale Merritt</p>
      <p>P 0400 555 817</p>
      <p class="gap">E dale@brindleyfitouts.com</p>
    </div>
  </div>

</div>
</body>
</html>
```